Lumen Coating business card for residential and commercial painting

A clean, professional design. Easy to read
Eye catching and elegant
Front could have some color variations
On the back of card I would like all black with signature logo

*Attached is my current business card and the items I want displayed

Contact Information for Business Card

Email, phone number, website, and owner name

Font styles to use
Serif

Requirements
Must have
• My logo with cool design and perhaps some paint splatter

```html
<!DOCTYPE html>
<html lang="en">
<head>
<meta charset="utf-8">
<title>Lumen Coating – Business Card</title>
<link href="https://fonts.googleapis.com/css2?family=Oswald:wght@400;500&family=Questrial&display=swap" rel="stylesheet">
<style>
  :root {
    --stage: #8f8f8f;
    --card: #ffffff;
    --charcoal: #363638;
    --brand-blue: #1172bb;
    --rule: #9a9a9a;
    --text: #2f2f31;
  }
  * { box-sizing: border-box; margin: 0; padding: 0; }
  html, body { width: 1200px; height: 1200px; overflow: hidden; }
  body { background: var(--stage); position: relative; font-family: "Questrial", sans-serif; }

  .card {
    position: absolute;
    top: 303px;
    width: 368px;
    height: 594px;
    background: var(--card);
    box-shadow: 3px 4px 6px rgba(0,0,0,0.35);
    overflow: hidden;
  }
  .card--front { left: 200px; }
  .card--back { left: 599px; width: 364px; }

  /* Front card */
  .front-band {
    position: absolute; left: 0; top: 0; width: 100%; height: 247px;
    background: var(--charcoal);
  }
  .front-brand {
    position: absolute; left: 0; width: 100%; top: 96px;
    text-align: center;
    font-family: "Oswald", sans-serif; font-weight: 500;
    font-size: 40px; letter-spacing: 1px;
    color: var(--brand-blue);
    text-transform: uppercase;
  }
  .price-label {
    position: absolute; left: 0; width: 100%; top: 455px;
    text-align: center;
    font-family: "Oswald", sans-serif; font-weight: 400;
    font-size: 30px; color: var(--brand-blue);
  }

  /* Back card */
  .brand-name {
    position: absolute; left: 0; width: 100%; top: 140px;
    text-align: center;
    font-family: "Oswald", sans-serif; font-weight: 500;
    font-size: 44px; letter-spacing: 0.5px;
    color: var(--charcoal);
    text-transform: uppercase;
  }
  .owner {
    position: absolute; left: 0; width: 100%; top: 383px; text-align: center;
  }
  .owner__name {
    font-family: "Oswald", sans-serif; font-weight: 400;
    font-size: 31px; line-height: 1.1; color: var(--brand-blue);
  }
  .owner__title { font-size: 16px; color: var(--text); margin-top: 1px; }

  .contact-icons {
    position: absolute; left: 0; width: 100%; top: 449px;
    display: flex; justify-content: center; align-items: center; gap: 4px;
  }
  .contact-icons .rule { width: 52px; height: 1px; background: var(--rule); margin: 0 3px; }
  .contact-icons svg { width: 25px; height: 25px; display: block; }

  .contact-details {
    position: absolute; left: 0; width: 100%; top: 484px;
    text-align: center; font-size: 15.5px; line-height: 21.5px; color: var(--text);
  }
  .contact-details .accent { color: var(--brand-blue); }
</style>
</head>
<body>

  <section class="card card--front">
    <div class="front-band"></div>
    <div class="front-brand">Lumen Coating</div>
    <div class="price-label">Price:</div>
  </section>

  <section class="card card--back">
    <div class="brand-name">Lumen Coating</div>

    <div class="owner">
      <div class="owner__name">Mateo "Matt"</div>
      <div class="owner__title">Owner-Licensed &amp; Insured</div>
    </div>

    <div class="contact-icons">
      <span class="rule"></span>
      <svg viewBox="0 0 25 25" aria-label="Phone">
        <rect width="25" height="25" rx="3" fill="var(--brand-blue)"/>
        <path d="M5 10 Q12.5 5 20 10 L19 12 L16 11 L16 9.5 Q12.5 8.5 9 9.5 L9 11 L6 12 Z" fill="#fff"/>
        <rect x="8" y="12" width="9" height="7" rx="1" fill="#fff"/>
      </svg>
      <svg viewBox="0 0 25 25" aria-label="Email">
        <rect width="25" height="25" rx="3" fill="var(--brand-blue)"/>
        <rect x="5" y="7.5" width="15" height="10" fill="none" stroke="#fff" stroke-width="1.3"/>
        <path d="M5 7.5 L12.5 13 L20 7.5 M5 17.5 L10.5 12 M20 17.5 L14.5 12" fill="none" stroke="#fff" stroke-width="1.1"/>
      </svg>
      <svg viewBox="0 0 25 25" aria-label="Website">
        <rect width="25" height="25" rx="3" fill="var(--brand-blue)"/>
        <circle cx="12.5" cy="12.5" r="7" fill="#fff"/>
        <path d="M9 8 Q11 9 10.5 11 Q9 12 10 14 L11 17 Q8 15 8 12 Z M13 7 Q16 8 15 10 L17 12 Q18 15 15 17 Q14 14 13 13 Z" fill="var(--brand-blue)"/>
      </svg>
      <span class="rule"></span>
    </div>

    <div class="contact-details">
      <div>93.482.5170</div>
      <div>lumencoatingtn@brushmail.com</div>
      <div>www.<span class="accent">lumencoatingtn</span>.com</div>
    </div>
  </section>

</body>
</html>
```